Dravolith Business Card

I have a logo that I would like to use to design the Business Card for Dravolith Construction LLC. We are a commercial general contractor in San Antonio Texas. Id like a simple and sleek design. Message me if you have any questions. Thanks

Industry/Entity Type

Contractor

```html
<!DOCTYPE html>
<html lang="en">
<head>
<meta charset="utf-8">
<title>Dravolith Business Card</title>
<link rel="stylesheet" href="https://fonts.googleapis.com/css2?family=Arimo:wght@400;700&display=swap">
<style>
  :root {
    --stage: #58595b;
    --paper: #ffffff;
    --brand-blue: #2f67b2;
    --brand-navy: #1f4a86;
    --soft-blue: #6f8ccc;
    --ink: #231f20;
    --ink-soft: #3a3a3a;
    --on-blue: #e6edf8;
    --accent-orange: #f26522;
  }
  * { margin: 0; padding: 0; box-sizing: border-box; }
  html, body {
    width: 1200px; height: 383px; overflow: hidden;
    background: var(--stage);
    font-family: "Arimo", Arial, sans-serif;
  }
  .card {
    position: absolute; top: 43px; width: 522px; height: 297px;
    background: var(--paper); overflow: hidden;
  }
  .card--front { left: 44px; }
  .card--back { left: 630px; }

  /* Front */
  .front__mark {
    position: absolute; left: 86px; top: 32px;
    width: 62px; height: 62px; background: var(--brand-blue);
  }
  .wordmark {
    position: absolute; right: 29px; top: 29px;
    color: var(--ink); font-weight: 700; text-align: right;
    font-size: 24px; line-height: 22px; letter-spacing: -0.3px;
  }
  .holder { position: absolute; left: 269px; top: 112px; }
  .holder__name { font-size: 17px; line-height: 20px; color: var(--ink); letter-spacing: 0.2px; }
  .holder__role { font-size: 12px; line-height: 14px; color: var(--ink-soft); margin-top: 1px; }
  .front__band {
    position: absolute; left: 0; right: 0; bottom: 0; height: 147px;
    background: var(--brand-blue);
  }
  .front__rule {
    position: absolute; left: 269px; top: 150px; width: 224px; height: 6px;
    background: var(--brand-navy);
  }
  .contact {
    position: absolute; color: var(--on-blue); font-size: 11px; line-height: 16px;
  }
  .contact__row { display: flex; align-items: flex-start; }
  .contact__icon { width: 25px; flex: none; padding-top: 2px; }
  .contact__icon svg { display: block; width: 11px; height: 11px; fill: var(--on-blue); }
  .contact--office { left: 27px; top: 170px; }
  .contact--office .gap { margin-top: 8px; }
  .contact--direct { left: 271px; top: 172px; }
  .contact--direct .contact__icon { width: 32px; }
  .contact--direct .gap { margin-top: 4px; }

  /* Back */
  .back__mark {
    position: absolute; left: 240px; top: 94px;
    width: 40px; height: 40px; border-radius: 50%; background: var(--soft-blue);
  }
  .back__name {
    position: absolute; left: 0; right: 0; top: 152px; text-align: center;
    color: var(--soft-blue); font-weight: 700; font-size: 18px; line-height: 17px;
  }
  .back__band {
    position: absolute; left: 0; right: 0; bottom: 0; height: 17px;
    background: var(--accent-orange);
  }
</style>
</head>
<body>

<section class="card card--front">
  <div class="front__mark"></div>
  <div class="wordmark">DRAVOLITH<br>CONSTRUCTION LLC</div>

  <div class="front__band"></div>
  <div class="front__rule"></div>

  <div class="holder">
    <p class="holder__name">Marel Quintas</p>
    <p class="holder__role">General Manager</p>
  </div>

  <div class="contact contact--office">
    <div class="contact__row">
      <span class="contact__icon"><svg viewBox="0 0 12 12"><path d="M2.5 1l2 2-1 1.5c.7 1.5 2 2.8 3.5 3.5L8.5 7l2 2-1.5 2C5 11 1 7 1 2.5z"/></svg></span>
      <span>+1 210 555 0147</span>
    </div>
    <div class="contact__row">
      <span class="contact__icon"><svg viewBox="0 0 12 12"><rect x="1" y="5" width="10" height="6" rx="1"/><rect x="3" y="1" width="6" height="3.5"/></svg></span>
      <span>+1 210 555 0182</span>
    </div>
    <div class="contact__row gap">
      <span class="contact__icon"><svg viewBox="0 0 12 12"><path d="M6 .5a5.5 5.5 0 1 0 0 11A5.5 5.5 0 0 0 6 .5zm0 1c.6.6 1.2 1.8 1.4 3.5H4.6C4.8 3.3 5.4 2.1 6 1.5zM1.6 6.5h2c.1 1.4.5 2.7 1.1 3.6a4.5 4.5 0 0 1-3.1-3.6zm0-1.5a4.5 4.5 0 0 1 3.1-3.6C4.1 2.3 3.7 3.6 3.6 5zm4.4 5.5c-.6-.6-1.2-1.8-1.4-4h2.8c-.2 2.2-.8 3.4-1.4 4zm1.3-.4c.6-.9 1-2.2 1.1-3.6h2a4.5 4.5 0 0 1-3.1 3.6zM8.4 5c-.1-1.4-.5-2.7-1.1-3.6A4.5 4.5 0 0 1 10.4 5z"/></svg></span>
      <span>www.dravolith.com</span>
    </div>
    <div class="contact__row gap">
      <span class="contact__icon"><svg viewBox="0 0 12 12"><path d="M6 .5A3.7 3.7 0 0 0 2.3 4.2C2.3 7 6 11.5 6 11.5S9.7 7 9.7 4.2A3.7 3.7 0 0 0 6 .5zm0 5a1.3 1.3 0 1 1 0-2.6 1.3 1.3 0 0 1 0 2.6z"/></svg></span>
      <span>Suite 6/ Level 4, 750 Alamo Plaza Drive,<br>San Antonio, TX 78205</span>
    </div>
  </div>

  <div class="contact contact--direct">
    <div class="contact__row">
      <span class="contact__icon"><svg viewBox="0 0 12 12"><path d="M3.5 0h5a1 1 0 0 1 1 1v10a1 1 0 0 1-1 1h-5a1 1 0 0 1-1-1V1a1 1 0 0 1 1-1zm.3 1.5v7h4.4v-7z"/></svg></span>
      <span>+1 210 555 0196</span>
    </div>
    <div class="contact__row gap">
      <span class="contact__icon"><svg viewBox="0 0 12 12"><path d="M.5 2.5h11v7H.5zm1 1v.3L6 6.8l4.5-3V3.5zm0 1.5v3.5h9V5L6 8z"/></svg></span>
      <span>marel-quintas@dravolith.com</span>
    </div>
  </div>
</section>

<section class="card card--back">
  <div class="back__mark"></div>
  <div class="back__name">DRAVOLITH<br>CONSTRUCTION LLC</div>
  <div class="back__band"></div>
</section>

</body>
</html>
```